A reimagined website for a cross-border tax firm

There are two aspects to this project for Brindlemoor Tax Advisory:
1) I need a logo update to accommodate increasing focus and specialization in my business. The byline under the name “Brindlemoor Tax Advisory” needs to change:
ORIGINAL: TAX SUPPORT FOR PUBLIC ACCOUNTING FIRMS
REVISED: CROSS-BORDER TAX SERVICES • U.S. & CANADA
2) I need a website “refresh” (see current website at www.levyhelpdesk.example) based on this logo – a new vision for a website with greater clarity, focus and organization. It should represent a re-envisioning of the current approach, and not the wholesale abandonment of the style represented there. I need it to be creative, compelling and attention grabbing, but still professional. This should, at a minimum, update any places where the old name/logo is used, but I want the redesign to go beyond this to something more intuitive. I need high quality separate PNG files of the various logo styles for use in various documents, but HTML coding would be a helpful but not necessary addition.

Target Market(s)

People in need of cross-border tax services - Canada and US

Coding

Number of Pages Required

Requirements
Must have
• Greater crispness, sharpness - higher resolution
• A more compelling, organized approach - make the wording and images more accessible to the website user (especially the staff bios, which have scroll bars now)
Nice to have
• Replacement of stock image with a true image of the Halifax skyline
Should not have
• Deviate from colour pattern represented in website logo of blue/orange
• Deviate from existing logo except for word replacement

```html
<!DOCTYPE html>
<html lang="en">
<head>
<meta charset="utf-8">
<title>Brindlemoor Tax Advisory</title>
<link href="https://fonts.googleapis.com/css2?family=Cinzel:wght@400;700&family=PT+Sans:ital,wght@0,400;0,700;1,400&display=swap" rel="stylesheet">
<style>
:root{
  --blue:#1e8fd6;
  --blue-dark:#14629f;
  --blue-deep:#0d3f6b;
  --orange:#f6a623;
  --orange-deep:#ee8d12;
  --orange-light:#fbc25a;
  --ink:#333a40;
  --muted:#6b7278;
  --white:#ffffff;
  --grey:#e9ecef;
}
*{box-sizing:border-box;margin:0;padding:0}
html,body{width:1200px;height:4489px;overflow:hidden;background:var(--white)}
body{position:relative;font-family:"PT Sans",Arial,sans-serif;color:var(--ink);font-size:14px}
.abs{position:absolute}
.mark{width:44px;height:44px;border:5px solid var(--orange);left:578px}
.btn{position:absolute;background:var(--orange);color:var(--white);font-family:"Cinzel",Georgia,serif;font-weight:700;font-size:19px;border-radius:30px;display:flex;align-items:center;justify-content:center;letter-spacing:1px}

/* top bar & nav */
.topbar{top:0;left:0;width:1200px;height:72px}
.topbar .phone{left:80px;top:10px;font-size:17px;color:var(--ink);display:flex;gap:10px;align-items:center}
.topbar .pay{right:70px;top:8px;font-family:"Cinzel",Georgia,serif;font-weight:700;font-size:20px;color:var(--blue-dark);display:flex;gap:12px;align-items:center}
.nav a{position:absolute;top:78px;height:44px;display:flex;align-items:center;font-size:16px;color:var(--ink);text-decoration:none;text-transform:uppercase;white-space:nowrap}
.nav .active{background:var(--orange);color:var(--white);border-radius:22px;padding:0 26px}
.brand{left:450px;top:8px;width:300px;height:140px;background:var(--white);text-align:center;z-index:3;overflow:hidden}
.brand .square{width:70px;height:70px;border:8px solid var(--orange);margin:6px auto 8px}
.brand .name{font-family:"Cinzel",Georgia,serif;font-weight:700;font-size:17px;color:var(--blue-deep);white-space:nowrap}
.brand .byline{font-size:9px;letter-spacing:.4px;color:var(--muted);margin-top:5px;white-space:nowrap}

/* hero */
.hero{top:145px;left:0;width:1200px;height:590px}
.hero-photo{top:0;left:30px;width:1170px;height:575px;border-radius:0 0 180px 0;background:linear-gradient(180deg,#2c3e55 0%,#4f6f8f 45%,#8aa6bf 75%,#3c5a78 100%)}
.hero h1{top:220px;left:0;width:1200px;text-align:center;color:var(--white);font-family:"Cinzel",Georgia,serif;font-weight:700;font-size:40px;line-height:1.3;letter-spacing:1px}
.hero h1 small{display:block;font-size:33px;font-weight:400}
.dots{top:365px;left:565px;display:flex;gap:10px}
.dots span{width:14px;height:14px;border-radius:50%;border:2px solid var(--white)}
.dots span.on{background:var(--orange);border-color:var(--orange)}

/* why choose */
.why{top:690px;left:0;width:1200px;height:372px;background:var(--blue)}
.why h2{top:28px;width:1200px;text-align:center;font-family:"Cinzel",Georgia,serif;font-size:42px;color:var(--orange-light)}
.why h2 b{color:var(--white);font-weight:400}
.card{top:110px;width:300px;height:190px;background:var(--blue);box-shadow:0 6px 14px rgba(0,30,70,.35);text-align:center;color:var(--white);font-family:"Cinzel",Georgia,serif;font-weight:700;font-size:20px}
.card svg{margin:22px auto 14px;display:block}

/* welcome */
.welcome .sub{top:1170px;width:1200px;text-align:center;font-family:"Cinzel",Georgia,serif;font-size:24px;color:var(--orange)}
.welcome h2{top:1202px;width:1200px;text-align:center;font-family:"Cinzel",Georgia,serif;font-size:44px;color:var(--blue-dark)}
.photo-meeting{top:1278px;left:215px;width:773px;height:248px;background:linear-gradient(90deg,#b9c2c9,#eef0f2 40%,#c4ccd3 70%,#59636d)}
.welcome p{top:1540px;left:190px;width:820px;text-align:center;font-size:14.5px;line-height:1.75;color:var(--ink)}

/* individuals */
.indiv{top:1787px;left:0;width:1200px;height:542px;border-radius:140px 0 0 0;background:linear-gradient(90deg,var(--orange-light),var(--orange) 60%,var(--orange-deep))}
.frame{background:var(--blue)}
.circle-photo{border-radius:50%;border:10px solid var(--white)}
.indiv h2{top:115px;right:75px;font-family:"Cinzel",Georgia,serif;font-size:46px;color:var(--blue-dark)}
.indiv p{right:75px;width:560px;text-align:right;color:var(--white);font-size:14.5px;line-height:1.75}
.btn-ghost{background:transparent;border:2px solid var(--white)}

/* team */
.team h2{top:2450px;width:1200px;text-align:center;font-family:"Cinzel",Georgia,serif;font-size:44px;color:var(--blue-dark)}
.team h2 span{color:var(--orange)}
.bio-photo{top:2529px;left:170px;width:272px;height:308px;background:linear-gradient(160deg,#6b7884,#2c3640)}
.bio{top:2550px;left:440px;width:578px;height:270px;background:var(--white);box-shadow:0 4px 16px rgba(0,0,0,.18);padding:20px 30px}
.bio h3{font-family:"Cinzel",Georgia,serif;font-size:20px;color:var(--blue-dark);font-weight:400}
.bio .lead{font-size:15px;margin-top:4px}
.bio p{font-size:13.5px;line-height:1.7;color:var(--muted);margin-top:14px;width:500px}
.bio .more{position:absolute;right:34px;bottom:16px;font-family:"Cinzel",Georgia,serif;font-size:14px;color:var(--orange);text-decoration:underline}
.side-arrow{top:2645px;width:30px;height:86px;background:var(--orange);display:flex;align-items:center;justify-content:center}

/* public firms */
.firms{top:2897px;left:0;width:1200px;height:570px;border-radius:0 140px 0 0;background:linear-gradient(90deg,var(--blue-dark),var(--blue) 55%,#4fb0e8)}
.firms h2{top:130px;left:80px;font-family:"Cinzel",Georgia,serif;font-size:46px;line-height:1.15;color:var(--white)}
.firms .tag{top:250px;left:80px;width:520px;color:var(--orange-light);font-weight:700;font-size:15px;line-height:1.4}
.firms p{top:300px;left:80px;width:560px;color:var(--white);font-size:14.5px;line-height:1.75}

/* testimonial */
.testi h2{top:3580px;width:1200px;text-align:center;font-family:"Cinzel",Georgia,serif;font-size:44px;color:var(--orange)}
.testi h2 span{color:var(--blue-dark)}
.testi blockquote{top:3690px;left:150px;width:900px;text-align:center;font-style:italic;font-size:14.5px;line-height:1.75;color:var(--ink)}
.testi cite{top:3785px;width:1200px;text-align:center;font-family:"Cinzel",Georgia,serif;font-style:normal;font-size:16px;color:var(--orange)}
.thumb{top:3850px;width:104px;height:104px;background:linear-gradient(180deg,#d8dde2,#9aa3ab)}
.thumb.on{top:3836px;width:110px;height:120px;border:4px solid var(--orange)}

/* contact */
.contact{top:4020px;left:0;width:1200px;height:416px;background:linear-gradient(90deg,#3a5f86,#5b86ad 45%,var(--orange) 100%)}
.contact h2{top:85px;right:80px;font-family:"Cinzel",Georgia,serif;font-size:44px;color:var(--white)}
.addr{color:var(--white);font-size:14px;line-height:1.45;text-align:right}
.tel{color:var(--white);font-size:18px;font-weight:700;display:flex;gap:14px;align-items:center}
.email{top:285px;left:560px;width:386px;height:54px;background:var(--white);color:var(--muted);font-size:14px;padding:0 18px;display:flex;align-items:center}
.subscribe{top:285px;left:946px;width:178px;height:54px;background:var(--orange);color:var(--white);font-family:"Cinzel",Georgia,serif;font-weight:700;font-size:20px;display:flex;align-items:center;justify-content:center}
.footer{top:4436px;left:0;width:1200px;height:53px;background:var(--blue);color:var(--white);font-size:14px;display:flex;align-items:center;justify-content:center}
</style>
</head>
<body>

<header>
  <div class="abs topbar">
    <div class="abs phone">
      <svg width="18" height="18" viewBox="0 0 24 24"><path d="M6.6 10.8a15 15 0 0 0 6.6 6.6l2.2-2.2a1 1 0 0 1 1-.25 11.4 11.4 0 0 0 3.6.6 1 1 0 0 1 1 1V20a1 1 0 0 1-1 1A17 17 0 0 1 3 4a1 1 0 0 1 1-1h3.5a1 1 0 0 1 1 1c0 1.25.2 2.45.6 3.6a1 1 0 0 1-.25 1z" fill="#1e8fd6"/></svg>
      (555) 014-2290
    </div>
    <div class="abs pay">
      <svg width="26" height="22" viewBox="0 0 26 22"><rect x="1" y="1" width="24" height="20" rx="2" fill="none" stroke="#f6a623" stroke-width="2"/><line x1="1" y1="7" x2="25" y2="7" stroke="#f6a623" stroke-width="3"/></svg>
      Payment Now
    </div>
  </div>
  <nav class="nav">
    <a class="active" style="left:80px">Home</a>
    <a style="left:195px">Our Team</a>
    <a style="left:302px">For Individuals</a>
    <a style="left:772px">For Public Accounting Firm</a>
    <a style="left:1043px">Contact</a>
  </nav>
  <div class="abs brand">
    <div class="square"></div>
    <div class="name">Brindlemoor Tax Advisory</div>
    <div class="byline">CROSS-BORDER TAX SERVICES • U.S. &amp; CANADA</div>
  </div>
</header>

<section class="abs hero">
  <svg class="abs" style="left:0;top:0" width="1200" height="600" viewBox="0 0 1200 600">
    <path d="M0 0 H1200 V430 Q1200 590 1040 590 H0 Z" fill="#1e8fd6"/>
    <path d="M0 300 Q10 560 220 590 L0 590 Z" fill="#f6a623"/>
  </svg>
  <div class="abs hero-photo" role="img" aria-label="City skyline of tall glass towers under a blue sky"></div>
  <h1 class="abs">Specializing in Tax Consultancy &amp;<small>Tax Planning for Your Clients</small></h1>
  <div class="abs dots"><span></span><span class="on"></span><span></span></div>
</section>

<section class="abs why">
  <h2 class="abs">Why Choose <b>Brindlemoor Tax</b></h2>
  <div class="abs card" style="left:120px">
    <svg width="80" height="90" viewBox="0 0 80 90" fill="none" stroke="#f6a623" stroke-width="4"><rect x="14" y="4" width="44" height="80" rx="6"/><rect x="30" y="30" width="46" height="30" rx="3" fill="#1e8fd6"/><line x1="30" y1="40" x2="76" y2="40"/></svg>
    Online Payment
  </div>
  <div class="abs card" style="left:464px">
    <svg width="80" height="90" viewBox="0 0 80 90" fill="none" stroke="#f6a623" stroke-width="4"><path d="M12 4 H52 L68 20 V86 H12 Z"/><path d="M52 4 V20 H68"/><line x1="22" y1="36" x2="58" y2="36"/><line x1="22" y1="50" x2="58" y2="50"/><line x1="22" y1="64" x2="46" y2="64"/></svg>
    Request a Quote
  </div>
  <div class="abs card" style="left:810px">
    <svg width="80" height="90" viewBox="0 0 80 90" fill="none" stroke="#f6a623" stroke-width="4"><path d="M22 14 L32 30 L26 38 Q34 54 46 60 L54 54 L70 64 L62 80 Q28 76 10 30 Z"/><path d="M46 18 Q62 22 64 38"/><path d="M46 6 Q74 10 76 38"/></svg>
    Callback Request
  </div>
</section>

<section class="welcome">
  <div class="abs mark" style="top:1108px"></div>
  <div class="abs sub">Welcome To</div>
  <h2 class="abs">Brindlemoor Tax Advisory</h2>
  <div class="abs photo-meeting" role="img" aria-label="Business team smiling around a meeting table"></div>
  <p class="abs">If you are an individual in need of tax support, we may be able to help you. Our services are designed to complement those offered by your existing accountant — we aim to work alongside your existing advisor(s) during those times when the complexity of your situation demands specialized advice. In general, we accept engagements only when the nature of the work demands our level of specialization and your existing accountant either doesn't want or isn't able to help you.</p>
  <div class="btn" style="top:1658px;left:503px;width:191px;height:54px">Learn More</div>
</section>

<section class="abs indiv">
  <div class="abs frame" style="left:120px;top:53px;width:413px;height:420px;border-radius:0 60px 0 60px"></div>
  <div class="abs circle-photo" role="img" aria-label="Business people shaking hands" style="left:170px;top:100px;width:320px;height:320px;background:radial-gradient(circle,#eef1f4,#9aa6b2)"></div>
  <div class="abs mark" style="left:1075px;top:65px;width:40px;height:40px;border-color:var(--blue-dark)"></div>
  <h2 class="abs">For Individuals</h2>
  <p class="abs" style="top:188px">If you are an individual in need of tax support, we may be able to help you. Our services are designed to complement those offered by your existing accountant — we aim to work alongside your existing advisor(s) during those times when the complexity of your situation demands specialized advice. In general, we accept engagements only when the nature of the work demands our level of specialization and your existing accountant either doesn't want or isn't able to help you.</p>
  <p class="abs" style="top:360px">We don't do bookkeeping or accounting. If you are running a business and you need what accountants call "<b>year end</b>" services.</p>
  <div class="btn btn-ghost" style="top:412px;left:937px;width:190px;height:54px">Learn More</div>
</section>

<section class="team">
  <div class="abs mark" style="top:2383px"></div>
  <h2 class="abs"><span>Meet</span> Our Team</h2>
  <div class="abs side-arrow" style="left:0"><svg width="12" height="18"><path d="M10 2 L3 9 L10 16" stroke="#fff" stroke-width="3" fill="none"/></svg></div>
  <div class="abs side-arrow" style="right:0"><svg width="12" height="18"><path d="M2 2 L9 9 L2 16" stroke="#fff" stroke-width="3" fill="none"/></svg></div>
  <div class="abs bio-photo" role="img" aria-label="Portrait of a team member in a dark suit"></div>
  <article class="abs bio">
    <div class="abs" style="right:30px;top:26px;width:36px;height:36px;border:4px solid var(--orange)"></div>
    <h3>Callum R. Weir, CPA, CGA, EA</h3>
    <div class="lead">Callum has been practicing tax for over 17 years.</div>
    <p>Educated at the University of Westbrook and Harlow College, he began his career in the Eastport office of Marrin Lowe LLP in September 1998. After a short period in the audit practice, he transferred to the tax division where he focused on Canadian corporate and US personal tax compliance (that is, the preparation and filing of tax returns).</p>
    <span class="more">Read More... »</span>
  </article>
</section>

<section class="abs firms">
  <div class="abs" style="left:80px;top:70px;width:40px;height:40px;border:5px solid var(--orange)"></div>
  <h2 class="abs">For Public Accounting<br>Firms</h2>
  <div class="abs tag">Our core business is providing tax support for public accounting firms (PAFs).</div>
  <p class="abs">In general, our PAF clients are small firms which are not large enough to have their own internal tax specialists. We can assist you as you compete with larger PAFs, by providing you with access to tax assistance on an "as needed" basis. We can perform research and assist with unusual or complex compliance. We can also help you with tax planning for your clients – both by developing plans and by overseeing their execution.</p>
  <div class="btn" style="top:421px;left:80px;width:185px;height:54px">Learn More</div>
  <div class="abs" style="left:673px;top:66px;width:413px;height:420px;background:var(--orange);border-radius:60px 0 60px 0"></div>
  <div class="abs circle-photo" role="img" aria-label="Group of business professionals standing together" style="left:720px;top:112px;width:320px;height:320px;background:radial-gradient(circle,#f4f6f8,#a8b3bd)"></div>
</section>

<section class="testi">
  <div class="abs mark" style="top:3512px"></div>
  <h2 class="abs">Our <span>Testimonial</span></h2>
  <svg class="abs" style="left:575px;top:3645px" width="50" height="40" viewBox="0 0 50 40"><path d="M4 38 V22 Q4 6 20 2 V10 Q12 12 12 20 H20 V38 Z M28 38 V22 Q28 6 44 2 V10 Q36 12 36 20 H44 V38 Z" fill="#fbc25a"/></svg>
  <blockquote class="abs">"Lorem Ipsum is simply dummy text of the printing and typesetting industry. Lorem Ipsum has been the industry's standard dummy text ever since the 1500s, when an unknown printer took a galley of type and scrambled it to make a type specimen book. It has survived not only five centuries, but also the leap into electronic typesetting, remaining essentially unchanged. "</blockquote>
  <cite class="abs">— Owen Marsh</cite>
  <svg class="abs" style="left:95px;top:3885px" width="16" height="30"><path d="M14 2 L3 15 L14 28" stroke="#b8bec4" stroke-width="2" fill="none"/></svg>
  <svg class="abs" style="left:1088px;top:3885px" width="16" height="30"><path d="M2 2 L13 15 L2 28" stroke="#b8bec4" stroke-width="2" fill="none"/></svg>
  <div class="abs thumb" role="img" aria-label="Client portrait" style="left:150px"></div>
  <div class="abs thumb" role="img" aria-label="Client portrait" style="left:285px"></div>
  <div class="abs thumb" role="img" aria-label="Client portrait" style="left:420px"></div>
  <svg class="abs" style="left:584px;top:3822px" width="32" height="16"><path d="M0 16 L16 0 L32 16 Z" fill="#f6a623"/></svg>
  <div class="abs thumb on" role="img" aria-label="Client portrait" style="left:545px"></div>
  <div class="abs thumb" role="img" aria-label="Client portrait" style="left:685px"></div>
  <div class="abs thumb" role="img" aria-label="Client portrait" style="left:820px"></div>
  <div class="abs thumb" role="img" aria-label="Client portrait" style="left:955px"></div>
</section>

<section class="abs contact" role="img" aria-label="Professionals working with documents at a desk, tinted blue and orange">
  <h2 class="abs">Contact Us</h2>
  <div class="abs addr" style="left:560px;top:158px;width:220px">48 Harbourline Drive, Unit 12<br>Eastport, Nova Scotia B0X 1A0</div>
  <svg class="abs" style="left:792px;top:164px" width="20" height="28" viewBox="0 0 20 28"><path d="M10 0 A10 10 0 0 1 20 10 C20 18 10 28 10 28 C10 28 0 18 0 10 A10 10 0 0 1 10 0 Z" fill="#f6a623"/><circle cx="10" cy="10" r="4" fill="#fff"/></svg>
  <div class="abs addr" style="left:860px;top:158px;width:210px">17 Millstone Road, Unit 3<br>Westvale, Nova Scotia B0X 2B0</div>
  <svg class="abs" style="left:1090px;top:164px" width="20" height="28" viewBox="0 0 20 28"><path d="M10 0 A10 10 0 0 1 20 10 C20 18 10 28 10 28 C10 28 0 18 0 10 A10 10 0 0 1 10 0 Z" fill="#f6a623"/><circle cx="10" cy="10" r="4" fill="#fff"/></svg>
  <div class="abs tel" style="left:648px;top:222px">(555) 014-2290</div>
  <svg class="abs" style="left:792px;top:222px" width="22" height="22" viewBox="0 0 24 24"><path d="M6.6 10.8a15 15 0 0 0 6.6 6.6l2.2-2.2a1 1 0 0 1 1-.25 11.4 11.4 0 0 0 3.6.6 1 1 0 0 1 1 1V20a1 1 0 0 1-1 1A17 17 0 0 1 3 4a1 1 0 0 1 1-1h3.5a1 1 0 0 1 1 1c0 1.25.2 2.45.6 3.6a1 1 0 0 1-.25 1z" fill="#1e8fd6"/></svg>
  <div class="abs tel" style="left:935px;top:222px">(555) 014-2290</div>
  <svg class="abs" style="left:1092px;top:222px" width="22" height="22" viewBox="0 0 24 24"><path d="M6.6 10.8a15 15 0 0 0 6.6 6.6l2.2-2.2a1 1 0 0 1 1-.25 11.4 11.4 0 0 0 3.6.6 1 1 0 0 1 1 1V20a1 1 0 0 1-1 1A17 17 0 0 1 3 4a1 1 0 0 1 1-1h3.5a1 1 0 0 1 1 1c0 1.25.2 2.45.6 3.6a1 1 0 0 1-.25 1z" fill="#1e8fd6"/></svg>
  <div class="abs email">Enter Email *</div>
  <div class="abs subscribe">Subscribe</div>
</section>

<footer class="abs footer">©Brindlemoor Tax Advisory Inc. - 2017. All Rights Reserved.</footer>

</body>
</html>
```